Stationery design for software development / consultancy company

We need stationary design based on company logo.

We are based in London, UK and we are providing integration solutions development / consultancy services for QVR integration projects across UK.

Our name refers two words - integration and grace - and it shows our clients our main specialization field and key characteristics of our solutions / products. We also would like to be associated with follow words: smart, reliable, unique.

Project delivery should include:
- Powerpoint template (needs to have a Cover Page, Table of Contents, 1-2 sample pages, and a Closing/Summary slide at the end)
- Letterhead A4 (Word template)
- Standard invoice A4 (Word template)
- With Compliments Slips A5 (Word template)
- Business card (adobe illustrator)

Attached is logo in vector (please use logo with white background!) and company details for printed stationery.

Target Market(s)

highly skilled IT professionals

Industry/Entity Type

Software

Requirements
Must have
• Clear background in all A4/A5 documents.
All text should be editable, i.e. I will need sources.
Nice to have
• I would prefer light, web 2.0 style colours, follow are in my main interest:
- combination of light grey and orange
- Logo colours
Should not have
• Please no watermarks on printed stationary

```html
<!DOCTYPE html>
<html lang="en">
<head>
<meta charset="utf-8">
<title>Meldora Limited — Stationery</title>
<link href="https://fonts.googleapis.com/css2?family=Open+Sans:wght@400;600;700&display=swap" rel="stylesheet">
<style>
:root{
  --orange:#f39221;
  --orange-deep:#ee8a1a;
  --ink:#222;
  --grey:#5a5a5a;
  --grey-light:#d2d2d2;
  --paper:#fff;
  --bg:#fff;
}
*{box-sizing:border-box;margin:0;padding:0}
html,body{width:1200px;height:1200px;overflow:hidden;background:var(--bg)}
body{position:relative;font-family:"Open Sans",Arial,sans-serif;color:var(--ink)}
.abs{position:absolute}
.brand{position:absolute;display:flex;align-items:center;gap:8px;font-weight:600;color:var(--grey);letter-spacing:-0.5px;line-height:1}
.brand .dot{border-radius:50%;background:var(--orange);flex:none}

/* invoice sheet */
.invoice{left:328px;top:55px;width:838px;height:1086px;background:var(--paper);box-shadow:0 2px 10px rgba(0,0,0,.18)}
.invoice .bar-top,.invoice .bar-bottom{position:absolute;left:0;width:100%;height:13px;background:var(--orange)}
.invoice .bar-top{top:0}.invoice .bar-bottom{bottom:0}
.contact{font-size:13px;line-height:16px}
.contact .row{display:flex;gap:8px}
.contact .label{color:var(--orange);font-weight:700;text-align:right}
.address{font-size:13px;line-height:16.3px}
.address b{font-weight:700}
.divider{position:absolute;width:1.5px;background:var(--orange)}
.invoice-title{font-size:58px;font-weight:700;color:var(--grey-light);line-height:1;letter-spacing:1px}
.tag{position:absolute;background:var(--orange);color:#fff;font-weight:700;font-size:15px;display:flex;align-items:center;justify-content:center}
.rule{position:absolute;height:1.5px;background:#333}
.band{position:absolute;background:var(--orange)}
.band-label{position:absolute;color:#fff;font-weight:700;font-size:15px;line-height:1}
.field{position:absolute;background:#fff}
.total-label{position:absolute;font-weight:700;font-size:15px;line-height:1;color:var(--ink)}
.thanks{position:absolute;left:0;width:100%;text-align:center;font-size:9.5px;font-weight:700;color:var(--grey)}

/* cards */
.card{position:absolute;left:21px;width:372px;height:212px;background:var(--paper);box-shadow:0 2px 10px rgba(0,0,0,.22);overflow:hidden}
.card .name{position:absolute;font-size:17px;line-height:1;white-space:nowrap}
.card .name b{font-weight:700}
.card .role{position:absolute;font-size:12.5px;line-height:1}
.card .contact{font-size:11.5px;line-height:16px}
.card .contact .label{font-size:14px;line-height:16px}
.card .address{font-size:11.5px;line-height:15px}
.company-line{position:absolute;font-weight:700;font-size:14px;color:var(--grey)}
.address-line{position:absolute;font-size:9.5px;white-space:nowrap}
.card-band{position:absolute;left:0;top:53px;width:100%;height:98px;background:var(--orange)}
.card-url{position:absolute;left:0;width:100%;text-align:center;font-size:20px;color:#888}
</style>
</head>
<body>

<!-- Invoice -->
<section class="abs invoice" aria-label="Invoice">
  <div class="bar-top"></div>
  <div class="brand" style="left:27px;top:35px;font-size:34px"><span class="dot" style="width:30px;height:30px"></span>meldora</div>
  <div class="abs contact" style="left:35px;top:85px">
    <div class="row"><span class="label" style="width:38px">Web</span><span>www.meldora.co.uk</span></div>
    <div class="row"><span class="label" style="width:38px">Email</span><span>enquiries@meldora.co.uk</span></div>
    <div class="row"><span class="label" style="width:38px">Tel</span><span>+44(0)121 555 0182</span></div>
  </div>
  <div class="divider" style="left:251px;top:40px;height:89px"></div>
  <div class="abs address" style="left:278px;top:35px">
    <b>Meldora Limited</b><br><b>48</b> Fern Court<br><b>77</b> Westbrook Lane<br>London<br><b>SE4 2RT</b><br>United Kingdom
  </div>
  <div class="abs invoice-title" style="left:588px;top:86px">INVOICE</div>

  <div class="tag" style="left:27px;top:207px;width:93px;height:33px">Customer</div>
  <div class="rule" style="left:130px;top:239px;width:224px"></div>
  <div class="tag" style="left:371px;top:207px;width:156px;height:33px">Shipping Address</div>
  <div class="rule" style="left:537px;top:239px;width:282px"></div>

  <div class="band" style="left:27px;top:272px;width:784px;height:75px"></div>
  <div class="band-label" style="left:37px;top:285px">Sales Person</div>
  <div class="band-label" style="left:240px;top:285px">Date Shipped</div>
  <div class="band-label" style="left:443px;top:285px">Shipped Via</div>
  <div class="band-label" style="left:649px;top:285px">Terms</div>
  <div class="field" style="left:37px;top:309px;width:149px;height:28px"></div>
  <div class="field" style="left:240px;top:309px;width:151px;height:28px"></div>
  <div class="field" style="left:443px;top:309px;width:151px;height:28px"></div>
  <div class="field" style="left:649px;top:309px;width:150px;height:28px"></div>

  <div class="band" style="left:27px;top:370px;width:784px;height:487px"></div>
  <div class="band-label" style="left:37px;top:383px">Quantity</div>
  <div class="band-label" style="left:123px;top:383px">Description</div>
  <div class="band-label" style="left:579px;top:383px">Unit Price</div>
  <div class="band-label" style="left:686px;top:383px">Amount</div>
  <div class="field" style="left:37px;top:407px;width:67px;height:433px"></div>
  <div class="field" style="left:123px;top:407px;width:438px;height:433px"></div>
  <div class="field" style="left:579px;top:407px;width:89px;height:433px"></div>
  <div class="field" style="left:686px;top:407px;width:115px;height:433px"></div>

  <div class="total-label" style="left:37px;top:889px">Subtotal</div>
  <div class="total-label" style="left:214px;top:889px">Shipping Fee</div>
  <div class="total-label" style="left:392px;top:889px">Sales Tax</div>
  <div class="total-label" style="left:650px;top:889px">Total Due</div>
  <div class="band" style="left:27px;top:910px;width:536px;height:48px"></div>
  <div class="field" style="left:37px;top:920px;width:149px;height:28px"></div>
  <div class="field" style="left:214px;top:920px;width:151px;height:28px"></div>
  <div class="field" style="left:392px;top:920px;width:151px;height:28px"></div>
  <div class="band" style="left:639px;top:910px;width:172px;height:48px"></div>
  <div class="field" style="left:649px;top:920px;width:150px;height:28px"></div>

  <div class="thanks" style="top:1050px">THANK YOU FOR YOUR BUSINESS</div>
  <div class="bar-bottom"></div>
</section>

<!-- Business card: front, split layout -->
<section class="card" style="top:389px" aria-label="Business card, split layout">
  <div class="brand" style="left:187px;top:22px;font-size:30px"><span class="dot" style="width:26px;height:26px"></span>meldora</div>
  <div class="name" style="left:0;width:210px;text-align:center;top:74px"><b>Daniel</b> Orwell</div>
  <div class="role" style="left:0;width:210px;text-align:center;top:99px">Director</div>
  <div class="abs contact" style="left:10px;top:120px">
    <div class="row"><span class="label" style="width:40px">Web</span><span>www.meldora.co.uk</span></div>
    <div class="row"><span class="label" style="width:40px">Email</span><span>enquiries@meldora.co.uk</span></div>
    <div class="row"><span class="label" style="width:40px">Tel</span><b>+44 (0) 121 - 555 - 0182</b></div>
    <div class="row"><span class="label" style="width:40px">Mob</span><b>+44 (0) 700 - 900 - 4417</b></div>
  </div>
  <div class="divider" style="left:205px;top:76px;height:119px"></div>
  <div class="abs address" style="left:221px;top:96px">
    <b>Meldora Limited</b><br><b>48</b> Fern Court<br><b>77</b> Westbrook Lane<br>London<br><b>SE4 2RT</b><br>United Kingdom
  </div>
</section>

<!-- Business card: front, centred layout -->
<section class="card" style="top:626px" aria-label="Business card, centred layout">
  <div class="brand" style="left:90px;top:18px;font-size:33px"><span class="dot" style="width:29px;height:29px"></span>meldora</div>
  <div class="name" style="right:203px;top:84px"><b>Daniel</b> Orwell</div>
  <div class="role" style="right:203px;top:103px">Director</div>
  <div class="divider" style="left:177px;top:82px;height:77px"></div>
  <div class="abs contact" style="left:187px;top:86px">
    <div class="row"><span class="label" style="width:34px;text-align:left">Web</span><span>www.meldora.co.uk</span></div>
    <div class="row"><span class="label" style="width:34px;text-align:left">Email</span><span>enquiries@meldora.co.uk</span></div>
    <div class="row"><span class="label" style="width:34px;text-align:left">Tel</span><span>+44 (0) 121 - 555 - 0182</span></div>
    <div class="row"><span class="label" style="width:34px;text-align:left">Mob</span><span>+44 (0) 700 - 900 - 4417</span></div>
  </div>
  <div class="company-line" style="left:15px;top:163px">Meldora Limited</div>
  <div class="address-line" style="left:15px;top:186px">48 Fern Court 77 Westbrook Lane, London SE4 2RT, United Kingdom</div>
</section>

<!-- Business card: back -->
<section class="card" style="top:857px" aria-label="Business card, back">
  <div class="card-band"></div>
  <div class="brand" style="left:68px;top:80px;font-size:44px;color:#fff"><span class="dot" style="width:36px;height:36px;background:#fff"></span>meldora</div>
  <div class="card-url" style="top:165px">www.meldora.co.uk</div>
</section>

</body>
</html>
```